Tidal Puffs. the aim is to sell vaping liquids based on mood or feelings

We are a company who sell vaping liquids. A designer from this site created a good logo for our company. I now need to use this logo and create a label to place onto vaping bottles. Unusually we will be selling vaping products based on Moods rather than flavours.

To be clear therefore the label should have our company Logo but then also reflect a particular type of Mood or feeling.

The designs for the various moods will then be printed as labels for our vaping bottles. We have 9 different Tidal Puffs (see below) that we intend to bring to the market and general public

i would therfore like designs for the following 9 feelings/moods:

Love
Chilled
Happy
Energy
Desire
Bliss
Lust
Calm
High

the first attachment has our stand alone Logo.

i will then send some attachments of ideas we were playing around with to point you in the right direction. i will need the designs to be very colourful and to reflect the mood.

i do like the love hart one so it doesn't necessarily mean that we need to have images of people on the label. i will leave it to the designers to use images they feel best reflects the specific mood

Target Market(s)

General public

Industry/Entity Type

Retail

Colors

Designer to choose colors to be used in the design.

Requirements
Must have
• my company logo on any design
Nice to have
• vibrant colours or image to match the particular mood vape

```html
<!DOCTYPE html>
<html lang="en">
<head>
<meta charset="utf-8">
<title>Tidal Puffs – Mood Labels</title>
<link rel="stylesheet" href="https://fonts.googleapis.com/css2?family=Bungee&family=Oswald:wght@400;600;700&family=Pacifico&display=swap">
<style>
  :root {
    --page: #f2f2f2;
    --ink: #ffffff;
    --ink-soft: #e6e6e6;
    --brand: #e8368f;
    --deep-blue: #1c1f8f;
    --indigo: #2a2070;
    --olive: #6f7a12;
    --lime: #b9c51f;
    --night: #0d0f1c;
    --alert: #e0262a;
    --frame: rgba(255,255,255,0.75);
  }
  * { box-sizing: border-box; margin: 0; padding: 0; }
  html, body { width: 773px; height: 1200px; overflow: hidden; }
  body {
    background: var(--page);
    font-family: "Oswald", sans-serif;
    color: var(--ink);
    position: relative;
  }
  .label {
    position: absolute;
    left: 126px;
    width: 520px;
    height: 372px;
    overflow: hidden;
    box-shadow: 0 2px 6px rgba(0,0,0,0.25);
  }
  .label--love    { top: 21px;  background: linear-gradient(100deg, #1a1d8c 0%, #24206e 35%, #5a5a22 70%, #a9b21c 100%); }
  .label--chilled { top: 414px; background: linear-gradient(100deg, #1f2a96 0%, #23307a 35%, #5f6a1c 70%, #a7b322 100%); }
  .label--happy   { top: 807px; background: linear-gradient(100deg, #2b2a86 0%, #3a2a6e 30%, #4c6a1a 65%, #a0b420 100%); }

  .label::after {
    content: "";
    position: absolute;
    inset: 6px;
    border: 1px solid var(--frame);
    pointer-events: none;
  }
  .shade {
    position: absolute;
    left: 0; right: 0; bottom: 0; height: 150px;
    background: linear-gradient(180deg, rgba(0,0,0,0) 0%, rgba(5,6,15,0.7) 100%);
  }
  .artwork { position: absolute; }

  .brand {
    position: absolute;
    left: 180px; top: 34px;
    width: 160px; height: 110px;
    display: flex; align-items: center; justify-content: center; gap: 6px;
  }
  .brand__dot {
    width: 12px; height: 12px; border-radius: 50%;
    background: var(--brand);
  }
  .brand__name {
    font-family: "Oswald", sans-serif;
    font-weight: 700;
    font-size: 30px;
    color: var(--brand);
    letter-spacing: 0.5px;
  }

  .mood-word {
    position: absolute;
    font-family: "Bungee", sans-serif;
    line-height: 0.92;
    background: linear-gradient(115deg, #f4e21b 0%, #2fbf3a 20%, #e5352b 38%, #7a3bd1 55%, #19a7e0 72%, #f08a1c 88%, #e8368f 100%);
    -webkit-background-clip: text;
    background-clip: text;
    color: transparent;
  }
  .label--love .mood-word    { left: 190px; top: 162px; font-size: 86px; }
  .label--chilled .mood-word { left: 158px; top: 178px; font-size: 76px; }
  .label--happy .mood-word   { left: 170px; top: 166px; font-size: 84px; }

  .premium {
    position: absolute;
    padding: 2px 6px;
    border: 1px solid currentColor;
    border-radius: 3px;
    font-family: "Pacifico", cursive;
    font-size: 12px;
    line-height: 1.05;
    text-align: center;
  }
  .label--love .premium    { left: 428px; top: 28px; color: var(--alert); }
  .label--chilled .premium { left: 432px; top: 160px; color: var(--ink); }
  .label--happy .premium   { left: 422px; top: 26px; color: var(--ink); }

  .safety-icons {
    position: absolute;
    left: 52px; top: 204px;
    display: grid;
    grid-template-columns: 22px 22px;
    gap: 14px 16px;
  }
  .safety-icons svg { width: 22px; height: 22px; }

  .warning {
    position: absolute;
    left: 36px; top: 286px;
    width: 118px;
  }
  .warning__title { font-size: 8px; font-weight: 700; letter-spacing: 0.3px; }
  .warning__body  { font-size: 5px; line-height: 1.35; color: var(--ink-soft); text-transform: uppercase; }

  .age-badge { position: absolute; left: 448px; top: 210px; width: 42px; height: 42px; }
  .age-notice {
    position: absolute; left: 442px; top: 266px;
    font-size: 8px; line-height: 1.1; font-weight: 600; text-transform: uppercase;
  }
  .age-notice strong { font-size: 11px; display: block; }
  .ratio {
    position: absolute; left: 450px; top: 300px;
    font-size: 13px; font-weight: 700; line-height: 1.2;
  }
</style>
</head>
<body>

<!-- LOVE -->
<section class="label label--love">
  <div class="artwork" role="img" aria-label="Faded blue photo of a couple embracing" style="left:20px;top:0;width:190px;height:170px;background:radial-gradient(ellipse at 45% 45%, rgba(90,100,200,0.55), rgba(30,30,120,0) 70%);"></div>
  <div class="artwork" role="img" aria-label="Glossy red hearts floating" style="left:340px;top:60px;width:120px;height:250px;background:radial-gradient(circle at 55% 28%, rgba(240,40,40,0.9) 0 14%, rgba(240,40,40,0) 26%), radial-gradient(circle at 62% 48%, rgba(230,30,30,0.85) 0 10%, rgba(230,30,30,0) 20%), radial-gradient(circle at 40% 80%, rgba(235,30,30,0.9) 0 18%, rgba(235,30,30,0) 30%);"></div>
  <div class="shade"></div>
  <div class="brand"><span class="brand__dot"></span><span class="brand__name">Tidal Puffs</span></div>
  <div class="mood-word">LO<br>VE</div>
  <div class="premium">Premium<br>Vape Liquid</div>
  <div class="safety-icons">
    <svg viewBox="0 0 22 22"><circle cx="11" cy="11" r="9.5" fill="none" stroke="#e0262a" stroke-width="1.5"/><path d="M7 11a4 4 0 0 1 7-2.6M15 11a4 4 0 0 1-7 2.6" fill="none" stroke="#fff" stroke-width="1.3"/></svg>
    <svg viewBox="0 0 22 22"><path d="M11 2 L20 11 L11 20 L2 11Z" fill="none" stroke="#e0262a" stroke-width="1.5"/><path d="M11 6.5v6M11 14.5v1.5" stroke="#fff" stroke-width="1.6"/></svg>
    <svg viewBox="0 0 22 22"><circle cx="11" cy="11" r="9.5" fill="none" stroke="#e0262a" stroke-width="1.5"/><line x1="4.5" y1="4.5" x2="17.5" y2="17.5" stroke="#e0262a" stroke-width="1.5"/><circle cx="11" cy="8" r="2" fill="#fff"/><rect x="9" y="10.5" width="4" height="5" fill="#fff"/></svg>
    <svg viewBox="0 0 22 22"><circle cx="9" cy="5" r="2" fill="#fff"/><path d="M9 7.5v7M9 9l-3 3M9 9l3 2" stroke="#fff" stroke-width="1.5" fill="none"/><rect x="13" y="11" width="6" height="8" fill="none" stroke="#fff" stroke-width="1.3"/></svg>
  </div>
  <div class="warning">
    <div class="warning__title">WARNING</div>
    <p class="warning__body">This liquid contains nicotine, a highly toxic and addictive substance. Keep well away from children and pets. For use only with electronic cigarettes and vaporisers. Not for sale to anyone under the age of 21.</p>
  </div>
  <svg class="age-badge" viewBox="0 0 42 42"><circle cx="21" cy="21" r="19" fill="none" stroke="#e0262a" stroke-width="3"/><line x1="8" y1="8" x2="34" y2="34" stroke="#e0262a" stroke-width="3"/><text x="21" y="14" font-size="4.5" text-anchor="middle" fill="#fff" font-family="Oswald, sans-serif">LESS THAN</text><text x="21" y="29" font-size="15" font-weight="700" text-anchor="middle" fill="#fff" font-family="Oswald, sans-serif">21</text></svg>
  <div class="age-notice">Under age sale<strong>Prohibited</strong></div>
  <div class="ratio">VG: 70<br>PG: 30</div>
</section>

<!-- CHILLED -->
<section class="label label--chilled">
  <div class="artwork" role="img" aria-label="Frozen icicles hanging along the top edge" style="left:0;top:0;width:520px;height:55px;background:linear-gradient(180deg, rgba(180,220,255,0.55), rgba(180,220,255,0));"></div>
  <div class="artwork" role="img" aria-label="Illustrated snowman with red hat and scarf" style="left:40px;top:65px;width:80px;height:115px;background:radial-gradient(ellipse at 50% 60%, rgba(245,245,250,0.9) 0 38%, rgba(245,245,250,0) 62%);"></div>
  <div class="artwork" role="img" aria-label="Faded photo of a smiling man wearing glasses" style="left:350px;top:48px;width:130px;height:160px;background:radial-gradient(ellipse at 50% 50%, rgba(200,190,90,0.55), rgba(200,190,90,0) 70%);"></div>
  <div class="shade"></div>
  <div class="brand"><span class="brand__dot"></span><span class="brand__name">Tidal Puffs</span></div>
  <div class="mood-word">CHI<br>LLED</div>
  <div class="premium">Premium<br>Vape Liquid</div>
  <div class="safety-icons">
    <svg viewBox="0 0 22 22"><circle cx="11" cy="11" r="9.5" fill="none" stroke="#e0262a" stroke-width="1.5"/><path d="M7 11a4 4 0 0 1 7-2.6M15 11a4 4 0 0 1-7 2.6" fill="none" stroke="#fff" stroke-width="1.3"/></svg>
    <svg viewBox="0 0 22 22"><path d="M11 2 L20 11 L11 20 L2 11Z" fill="none" stroke="#e0262a" stroke-width="1.5"/><path d="M11 6.5v6M11 14.5v1.5" stroke="#fff" stroke-width="1.6"/></svg>
    <svg viewBox="0 0 22 22"><circle cx="11" cy="11" r="9.5" fill="none" stroke="#e0262a" stroke-width="1.5"/><line x1="4.5" y1="4.5" x2="17.5" y2="17.5" stroke="#e0262a" stroke-width="1.5"/><circle cx="11" cy="8" r="2" fill="#fff"/><rect x="9" y="10.5" width="4" height="5" fill="#fff"/></svg>
    <svg viewBox="0 0 22 22"><circle cx="9" cy="5" r="2" fill="#fff"/><path d="M9 7.5v7M9 9l-3 3M9 9l3 2" stroke="#fff" stroke-width="1.5" fill="none"/><rect x="13" y="11" width="6" height="8" fill="none" stroke="#fff" stroke-width="1.3"/></svg>
  </div>
  <div class="warning">
    <div class="warning__title">WARNING</div>
    <p class="warning__body">This liquid contains nicotine, a highly toxic and addictive substance. Keep well away from children and pets. For use only with electronic cigarettes and vaporisers. Not for sale to anyone under the age of 21.</p>
  </div>
  <svg class="age-badge" viewBox="0 0 42 42"><circle cx="21" cy="21" r="19" fill="none" stroke="#e0262a" stroke-width="3"/><line x1="8" y1="8" x2="34" y2="34" stroke="#e0262a" stroke-width="3"/><text x="21" y="14" font-size="4.5" text-anchor="middle" fill="#fff" font-family="Oswald, sans-serif">LESS THAN</text><text x="21" y="29" font-size="15" font-weight="700" text-anchor="middle" fill="#fff" font-family="Oswald, sans-serif">21</text></svg>
  <div class="age-notice">Under age sale<strong>Prohibited</strong></div>
  <div class="ratio">VG: 70<br>PG: 30</div>
</section>

<!-- HAPPY -->
<section class="label label--happy">
  <div class="artwork" role="img" aria-label="Photo of a laughing woman in colourful smoke" style="left:20px;top:0;width:150px;height:230px;background:radial-gradient(ellipse at 50% 45%, rgba(190,120,110,0.5), rgba(120,60,140,0) 70%);"></div>
  <div class="artwork" role="img" aria-label="Green splash illustration of a jumping dancer" style="left:335px;top:40px;width:150px;height:250px;background:radial-gradient(ellipse at 50% 45%, rgba(60,200,60,0.65), rgba(60,200,60,0) 68%);"></div>
  <div class="shade"></div>
  <div class="brand"><span class="brand__dot"></span><span class="brand__name">Tidal Puffs</span></div>
  <div class="mood-word">HA<br>PPY</div>
  <div class="premium">Premium<br>Vape Liquid</div>
  <div class="safety-icons">
    <svg viewBox="0 0 22 22"><circle cx="11" cy="11" r="9.5" fill="none" stroke="#e0262a" stroke-width="1.5"/><path d="M7 11a4 4 0 0 1 7-2.6M15 11a4 4 0 0 1-7 2.6" fill="none" stroke="#fff" stroke-width="1.3"/></svg>
    <svg viewBox="0 0 22 22"><path d="M11 2 L20 11 L11 20 L2 11Z" fill="none" stroke="#e0262a" stroke-width="1.5"/><path d="M11 6.5v6M11 14.5v1.5" stroke="#fff" stroke-width="1.6"/></svg>
    <svg viewBox="0 0 22 22"><circle cx="11" cy="11" r="9.5" fill="none" stroke="#e0262a" stroke-width="1.5"/><line x1="4.5" y1="4.5" x2="17.5" y2="17.5" stroke="#e0262a" stroke-width="1.5"/><circle cx="11" cy="8" r="2" fill="#fff"/><rect x="9" y="10.5" width="4" height="5" fill="#fff"/></svg>
    <svg viewBox="0 0 22 22"><circle cx="9" cy="5" r="2" fill="#fff"/><path d="M9 7.5v7M9 9l-3 3M9 9l3 2" stroke="#fff" stroke-width="1.5" fill="none"/><rect x="13" y="11" width="6" height="8" fill="none" stroke="#fff" stroke-width="1.3"/></svg>
  </div>
  <div class="warning">
    <div class="warning__title">WARNING</div>
    <p class="warning__body">This liquid contains nicotine, a highly toxic and addictive substance. Keep well away from children and pets. For use only with electronic cigarettes and vaporisers. Not for sale to anyone under the age of 21.</p>
  </div>
  <svg class="age-badge" viewBox="0 0 42 42"><circle cx="21" cy="21" r="19" fill="none" stroke="#e0262a" stroke-width="3"/><line x1="8" y1="8" x2="34" y2="34" stroke="#e0262a" stroke-width="3"/><text x="21" y="14" font-size="4.5" text-anchor="middle" fill="#fff" font-family="Oswald, sans-serif">LESS THAN</text><text x="21" y="29" font-size="15" font-weight="700" text-anchor="middle" fill="#fff" font-family="Oswald, sans-serif">21</text></svg>
  <div class="age-notice">Under age sale<strong>Prohibited</strong></div>
  <div class="ratio">VG: 70<br>PG: 30</div>
</section>

</body>
</html>
```